Design a newsletter for a crypto gateway payment company

The project is about making the design for a newsletter (sent by email) for a crypto payment gateway. The design should include all usual and necessary parts found in a newsletter (header, one main article with illustration and link to the full content, some secondary articles with or without illustration and link to the company blog, footer with links to unsubscribe page and various information about the company, section separator, secondary articles ...).
The design may re-use some elements from the company web site https://vornexpay.io, but feel free to innovate.
The design should be responsive and be as good in all email clients and all sizes of display from handset to desktop with everything in between.
I've added a few screenshot of the previous newsletter as they were sent to users.
Good luck and be an artist. No AI stuff, please.

```html
<!DOCTYPE html>
<html lang="en">
<head>
<meta charset="utf-8">
<title>The VornexPay Times — March 2024</title>
<link href="https://fonts.googleapis.com/css2?family=Roboto:wght@400;500;700&display=swap" rel="stylesheet">
<style>
:root{
  --navy:#18184a;
  --ink:#1f2a4d;
  --body:#555a66;
  --gold:#ffc107;
  --orange:#ffa41b;
  --white:#ffffff;
  --band:#f4f6f9;
  --footer:#dde6f0;
  --illus-blue:#e8f1f8;
  --illus-gold:#fbe3a6;
}
*{margin:0;padding:0;box-sizing:border-box}
html,body{width:1158px;height:1200px;overflow:hidden;background:var(--white);font-family:"Roboto",Arial,sans-serif}
.newsletter{position:relative;width:1158px;height:1200px;background:var(--white)}
.masthead{position:absolute;left:0;top:0;width:1158px;height:146px;background:var(--navy);color:var(--white)}
.masthead__name{position:absolute;left:97px;top:50px;font-size:40px;font-weight:500;letter-spacing:-0.5px}
.masthead__date{position:absolute;right:60px;top:58px;font-size:20px;font-weight:400}
.hero{position:absolute;left:0;top:146px;width:1158px;height:439px;overflow:hidden}
.hero__blob{position:absolute;left:-80px;top:40px}
.hero__title{position:absolute;left:92px;top:48px;width:520px;font-size:34px;line-height:46px;font-weight:500;color:var(--ink)}
.hero__text{position:absolute;left:92px;top:147px;width:480px;font-size:15px;line-height:24px;color:var(--body)}
.hero__list{position:absolute;left:92px;top:240px;list-style:none}
.hero__list li{position:relative;padding-left:21px;font-size:15px;color:var(--body);height:35px;line-height:22px}
.hero__list li::before{content:"";position:absolute;left:0;top:6px;width:12px;height:12px;border-radius:50%;background:var(--orange)}
.btn{position:absolute;display:block;background:linear-gradient(90deg,var(--orange),var(--gold));color:var(--white);font-weight:700;text-transform:uppercase;text-align:center;text-decoration:none}
.hero__btn{left:92px;top:363px;width:121px;height:43px;line-height:43px;font-size:11px;border-radius:2px;box-shadow:0 6px 12px rgba(255,164,27,.3)}
.hero__art{position:absolute;left:598px;top:63px;width:460px;height:327px;border-radius:48% 52% 40% 60%/55% 45% 55% 45%;background:radial-gradient(circle at 50% 55%,var(--illus-blue),#f4f8fb 70%,var(--white))}
.divider{position:absolute;left:0;top:585px;width:1158px;height:20px;background:var(--band)}
.article{position:absolute;width:520px;height:180px}
.article__title{position:absolute;left:0;top:0;width:260px;font-size:17px;line-height:21px;font-weight:500;color:var(--ink)}
.article__text{position:absolute;left:0;top:50px;width:225px;font-size:7.5px;line-height:11px;color:var(--body)}
.article__btn{left:0;width:70px;height:20px;line-height:20px;font-size:5.5px;border-radius:1px}
.article__art{position:absolute;border-radius:50%}
.a1{left:90px;top:665px}
.a2{left:629px;top:684px}
.a3{left:90px;top:888px}
.a4{left:629px;top:868px}
.art-warm{background:radial-gradient(circle,var(--illus-gold),#fdf3db 60%,var(--white) 72%)}
.art-cool{background:radial-gradient(circle,#dcebf3,#eef5f9 60%,var(--white) 72%)}
.art-green{background:radial-gradient(circle,#e4f1d9,#f1f8ec 60%,var(--white) 72%)}
.utility{position:absolute;left:0;top:1066px;width:1158px;text-align:center;font-size:14px;color:#333}
.utility a{color:#333;text-decoration:underline}
.utility span{margin:0 14px}
.footer{position:absolute;left:0;top:1107px;width:1158px;height:93px;background:var(--footer);font-size:14px;color:#222}
.footer__copy{position:absolute;left:86px;top:33px}
.footer__links{position:absolute;right:82px;top:33px}
.footer__links a{color:#222;text-decoration:none}
.footer__links span{margin:0 14px}
</style>
</head>
<body>
<div class="newsletter">
  <header class="masthead">
    <div class="masthead__name">The VornexPay Times</div>
    <div class="masthead__date">March 2024</div>
  </header>

  <section class="hero">
    <svg class="hero__blob" width="620" height="420" viewBox="0 0 620 420" aria-hidden="true">
      <path d="M60 40 C220 0 420 30 520 120 C600 200 560 330 430 380 C300 420 120 400 60 320 C10 250 -20 70 60 40Z" fill="#f3f8fc"/>
    </svg>
    <h1 class="hero__title">We Are Leading International Digital Currency Agency</h1>
    <p class="hero__text">This should be used to tell a story and let your users know a little more about your product or service. How can you benefit them? convince them to use your service.</p>
    <ul class="hero__list">
      <li>We Are Passionate And Creative</li>
      <li>Open Source And Free Software</li>
      <li>Very Fast And Reliable</li>
    </ul>
    <a class="btn hero__btn" href="https://vornexpay.io">Learn More</a>
    <div class="hero__art" role="img" aria-label="Illustration of digital coins above a laptop with a security shield, a payment card and a rising bar chart"></div>
  </section>

  <div class="divider"></div>

  <article class="article a1">
    <h2 class="article__title">Invest In Cryptocoin<br>Easy Way To Trade Bitcoin.</h2>
    <p class="article__text">Launch your campaign and benefit from our expertise on designing and managing conversion centered landing pages.</p>
    <a class="btn article__btn" style="top:82px" href="https://vornexpay.io">Get Started Now</a>
    <div class="article__art art-warm" role="img" aria-label="Illustration of two people with a laptop sitting on stacks of gold coins" style="left:237px;top:-14px;width:190px;height:150px"></div>
  </article>

  <article class="article a2">
    <h2 class="article__title">Banking Platform That<br>Enables Currency Solutions.</h2>
    <p class="article__text">This should be used to tell a story and let your users know a little more about your product or service. How can you benefit them? convince them to use your service.</p>
    <a class="btn article__btn" style="top:85px" href="https://vornexpay.io">Learn More</a>
    <div class="article__art art-cool" role="img" aria-label="Illustration of a hand holding a phone with banknotes, coins and a shopping cart" style="left:248px;top:-25px;width:225px;height:150px"></div>
  </article>

  <article class="article a3">
    <h2 class="article__title">Banking Platform That<br>Enables Currency Solutions.</h2>
    <p class="article__text">This should be used to tell a story and let your users know a little more about your product or service. How can you benefit them? convince them to use your service.</p>
    <a class="btn article__btn" style="top:85px" href="https://vornexpay.io">Learn More</a>
    <div class="article__art art-green" role="img" aria-label="Illustration of a person beside plants and large coins with a growth chart" style="left:237px;top:-49px;width:190px;height:178px"></div>
  </article>

  <article class="article a4">
    <h2 class="article__title">Invest In Cryptocoin<br>Easy Way To Trade Bitcoin.</h2>
    <p class="article__text">Launch your campaign and benefit from our expertise on designing and managing conversion centered landing pages.</p>
    <a class="btn article__btn" style="top:82px" href="https://vornexpay.io">Get Started Now</a>
    <div class="article__art art-warm" role="img" aria-label="Illustration of a businessman with a briefcase under floating coins and a rising arrow" style="left:248px;top:-22px;width:200px;height:168px"></div>
  </article>

  <nav class="utility">
    <a href="https://vornexpay.io">Unsubscribe</a><span>|</span><a href="https://vornexpay.io">Manage Preferences</a>
  </nav>

  <footer class="footer">
    <div class="footer__copy">© VornexPay Technologies Pte. Ltd.2024 | All Rights Reserved</div>
    <div class="footer__links">
      <a href="https://vornexpay.io">About Us</a><span>|</span><a href="https://vornexpay.io">Contact Us</a><span>|</span><a href="https://vornexpay.io">Privacy Policy</a>
    </div>
  </footer>
</div>
</body>
</html>
```